Lumenfield Holdings

Professional looking business card using darker colours
I do not yet have a logo for the company so feel free to suggest
The business is based on consultancy and project management
Based in Melbourne
Business card can omit the word "Holdings" and can be Lumenfield consulting etc.

Business

Contact Name on card : Tom Verisco Contact number : +61412 305 617 Email address will be confirmed shortly.

```html
<!DOCTYPE html>
<html lang="en">
<head>
<meta charset="utf-8">
<title>Lumenfield Consulting – Business Card</title>
<link href="https://fonts.googleapis.com/css2?family=Montserrat:wght@600&family=Open+Sans:wght@400;700&display=swap" rel="stylesheet">
<style>
  :root {
    --backdrop: #e6e3de;
    --card-white: #ffffff;
    --card-grey: #e4e6e9;
    --navy: #0f4a7d;
    --navy-deep: #0a3862;
    --ink: #3a3f45;
    --brand-blue: #1d4f80;
  }
  * { margin: 0; padding: 0; box-sizing: border-box; }
  html, body { width: 1200px; height: 1023px; overflow: hidden; }
  body {
    background: var(--backdrop);
    position: relative;
    font-family: "Open Sans", Arial, sans-serif;
  }
  .card {
    position: absolute;
    width: 620px;
    height: 354px;
    border-radius: 4px;
    overflow: hidden;
    box-shadow: 0 10px 28px rgba(0,0,0,0.18);
  }
  .card-front {
    left: 60px; top: 110px;
    background: linear-gradient(135deg, var(--card-white) 0%, var(--card-white) 45%, var(--card-grey) 100%);
  }
  .card-back {
    left: 520px; top: 560px;
    background: linear-gradient(160deg, var(--navy) 0%, var(--navy-deep) 100%);
    display: flex;
    align-items: center;
    justify-content: center;
  }
  .swoosh { position: absolute; left: 0; top: 0; }
  .contact {
    position: absolute;
    right: 34px; top: 30px;
    text-align: right;
    color: var(--ink);
    font-size: 12.5px;
    line-height: 1.55;
  }
  .contact-name {
    font-weight: 700;
    font-size: 24px;
    color: var(--brand-blue);
    line-height: 1.1;
  }
  .contact-title { font-size: 12.5px; margin-bottom: 12px; }
  .contact-line { display: flex; justify-content: flex-end; align-items: center; gap: 8px; }
  .contact-icon {
    width: 13px; height: 13px;
    border-radius: 2px;
    background: var(--brand-blue);
    display: inline-flex; align-items: center; justify-content: center;
  }
  .address { margin-top: 12px; }
  .brand {
    font-family: "Montserrat", Arial, sans-serif;
    font-weight: 600;
    text-transform: uppercase;
    display: flex;
    align-items: center;
    gap: 14px;
  }
  .brand-mark { width: 16px; height: 16px; flex: none; }
  .brand-text { display: flex; flex-direction: column; line-height: 1.1; }
  .brand-name { letter-spacing: 2px; }
  .brand-sub { font-size: 0.5em; letter-spacing: 0.9em; margin-top: 4px; }
  .brand-front {
    position: absolute;
    left: 40px; top: 190px;
    color: var(--brand-blue);
    font-size: 30px;
  }
  .brand-front .brand-mark { background: var(--brand-blue); }
  .brand-back { color: #ffffff; font-size: 34px; }
  .brand-back .brand-mark { background: #ffffff; }
</style>
</head>
<body>

  <section class="card card-front">
    <svg class="swoosh" width="620" height="354" viewBox="0 0 620 354" aria-hidden="true">
      <path d="M0 354 L0 330 C180 300 420 290 620 200 L620 354 Z" fill="#c9ccd1"/>
      <path d="M0 354 L0 342 C200 320 430 305 620 225 L620 354 Z" fill="var(--navy)"/>
    </svg>

    <div class="contact">
      <div class="contact-name">Tom Verisco</div>
      <div class="contact-title">CEO and Creative Director</div>
      <div class="contact-line">+61412 305 617
        <span class="contact-icon"><svg width="9" height="9" viewBox="0 0 10 10"><path d="M2 1 L4 1 L4.6 3.2 L3.4 4 C4 5.4 4.8 6.2 6 6.6 L6.8 5.4 L9 6 L9 8 C9 8.6 8.6 9 8 9 C4.2 8.6 1.4 5.8 1 2 C1 1.4 1.4 1 2 1 Z" fill="#fff"/></svg></span>
      </div>
      <div class="contact-line">+61398 214 560
        <span class="contact-icon"><svg width="9" height="9" viewBox="0 0 10 10"><rect x="1" y="3" width="8" height="5" fill="#fff"/><rect x="3" y="1" width="4" height="2" fill="#fff"/></svg></span>
      </div>
      <div class="contact-line">tom@lumenfieldconsulting.com
        <span class="contact-icon"><svg width="9" height="9" viewBox="0 0 10 10"><rect x="1" y="2.5" width="8" height="5.5" fill="#fff"/><path d="M1 2.5 L5 5.5 L9 2.5" stroke="var(--brand-blue)" fill="none"/></svg></span>
      </div>
      <div class="contact-line">www.lumenfieldconsulting.com
        <span class="contact-icon"><svg width="9" height="9" viewBox="0 0 10 10"><circle cx="5" cy="5" r="3.8" stroke="#fff" fill="none"/><path d="M1.2 5 H8.8 M5 1.2 V8.8" stroke="#fff"/></svg></span>
      </div>
      <div class="address">
        420 Collins Street<br>
        Suite 600<br>
        Melbourne, Victoria 3000
      </div>
    </div>

    <div class="brand brand-front">
      <span class="brand-mark"></span>
      <span class="brand-text"><span class="brand-name">Lumenfield</span><span class="brand-sub">Consulting</span></span>
    </div>
  </section>

  <section class="card card-back">
    <div class="brand brand-back">
      <span class="brand-mark"></span>
      <span class="brand-text"><span class="brand-name">Lumenfield</span><span class="brand-sub">Consulting</span></span>
    </div>
  </section>

</body>
</html>
```